Lip balm label

4 different kinds with a blend of essential oils. Cravings, Energy, Anxiety and Sensual. No preservatives or engineered products. Need different colored labels for each one. Maybe lavender or purple for stress, green or orange for appetite, red for energy and black for sensual. Or just use your professional judgement. Must fit on small lip balm tube

Target Market(s)

Young and old adults

Industry/Entity Type

Cosmetics

Logo Text

Mouthgrove

Logo styles of interest
Wordmark Logo
Font styles to use
Decorative

Requirements
Must have
• Name of company (KoDu Organics), 100% Organic, list of ingredients in each one, weight is 0.15 oz, made with Essential Oils, soothing and moisturizing,
• Lip Balm
Nice to have
• Made in USA, satisfaction guaranteed

```html
<!DOCTYPE html>
<html lang="en">
<head>
<meta charset="utf-8">
<title>Mouthgrove Lip Balm Label – Energy</title>
<link rel="stylesheet" href="https://fonts.googleapis.com/css2?family=Josefin+Sans:wght@300&family=Raleway:wght@400;700&display=swap">
<style>
  :root {
    --purple: #7b5fae;
    --green: #7aab45;
    --leaf: #86b04e;
    --badge: #d9444d;
    --white: #ffffff;
  }
  html, body {
    margin: 0;
    padding: 0;
    overflow: hidden;
    background: var(--white);
  }
  .label {
    position: relative;
    width: 1200px;
    height: 1137px;
    overflow: hidden;
    background: var(--white);
    font-family: "Raleway", sans-serif;
  }
  .vertical {
    position: absolute;
    writing-mode: vertical-rl;
    transform: rotate(180deg);
    white-space: nowrap;
    text-align: center;
    margin: 0;
  }
  .foliage {
    position: absolute;
  }
  .foliage--top {
    left: 0; top: 0; width: 262px; height: 202px;
    background: radial-gradient(ellipse at 30% 20%, var(--leaf), rgba(134,176,78,0) 70%);
  }
  .foliage--bottom {
    left: 1020px; top: 908px; width: 180px; height: 229px;
    background: radial-gradient(ellipse at 70% 70%, var(--leaf), rgba(134,176,78,0) 72%);
  }
  .brand-name {
    left: 196px; top: 130px; width: 210px; height: 890px;
    font-family: "Josefin Sans", sans-serif;
    font-weight: 300;
    font-size: 172px;
    line-height: 210px;
    color: var(--purple);
  }
  .company-name {
    left: 405px; top: 120px; width: 45px; height: 502px;
    font-size: 34px;
    line-height: 45px;
    letter-spacing: 0.32em;
    color: var(--purple);
  }
  .natural-tag {
    position: absolute;
    left: 474px; top: 129px; width: 62px; height: 433px;
    background: var(--purple);
  }
  .natural-tag .vertical {
    left: 0; top: 0; width: 62px; height: 433px;
    font-size: 38px;
    line-height: 62px;
    color: var(--white);
  }
  .origin-badge {
    position: absolute;
    left: 562px; top: 30px; width: 180px; height: 225px;
  }
  .net-weight {
    left: 598px; top: 465px; width: 48px; height: 202px;
    font-size: 46px;
    font-weight: 700;
    line-height: 48px;
    color: var(--green);
  }
  .product-description {
    left: 708px; top: 225px; width: 104px; height: 683px;
    font-size: 38px;
    line-height: 52px;
    color: var(--purple);
  }
  .ingredients-frame {
    position: absolute;
    left: 840px; top: 168px; width: 180px; height: 785px;
    border: 6px solid var(--purple);
  }
  .flavour-name {
    left: 45px; top: 795px; width: 50px; height: 225px;
    font-size: 44px;
    font-weight: 700;
    line-height: 50px;
    color: var(--purple);
  }
  .flavour-swatch {
    position: absolute;
    left: 0; top: 1059px; width: 140px; height: 78px;
    background: var(--purple);
  }
</style>
</head>
<body>
  <div class="label">
    <div class="foliage foliage--top" role="img" aria-label="Green leaf illustration in the corner"></div>

    <h1 class="vertical brand-name">Mouthgrove</h1>
    <p class="vertical company-name">KODU ORGANICS</p>

    <div class="natural-tag">
      <p class="vertical">100% NATURAL</p>
    </div>

    <svg class="origin-badge" viewBox="0 0 180 225" aria-label="Origin badge">
      <rect x="30" y="40" width="120" height="150" rx="8" fill="var(--badge)" transform="rotate(-25 90 115)"/>
    </svg>

    <p class="vertical net-weight">0.15 OZ</p>

    <p class="vertical product-description">MOISTURIZING LIP BALM<br>MADE WITH ESSENTIAL OILS</p>

    <div class="ingredients-frame"></div>

    <p class="vertical flavour-name">ENERGY</p>
    <div class="flavour-swatch"></div>

    <div class="foliage foliage--bottom" role="img" aria-label="Green leaf illustration in the corner"></div>
  </div>
</body>
</html>
```